Fence Flyer to Attract More Sales During Winter

We need a new flyer made that we can distribute to residential mailboxes. The flyer is to promote our Frostline Picket Days. We like simply designs, and we would like the flyer to showcase a lot of our fence photos. More of our photos are online at our website at www.getbramblerail.com - our new address needs to also be featured on the flyer - 436 Quillen rd, Monroe, NC 28117. I do want the words "FROSTLINE PICKET DAYS" to be dominate on the flyer with the description "Wood fences starting at $12/FT!" Please look through our Facebook page and our website to gather more photos or information. We are flexible on colors, nothing to fancy - simple flyer design please.

Target Market(s)

Residential homeowners that need a new fence to enclose their yard for safety, security or decorative

Industry/Entity Type

Residential Construction

Font styles to use
Sans Serif

Colors

Designer to choose colors to be used in the design.

Requirements
Must have
• Frostline Picket Days
• Contact information for the business
• "Come visit our outdoor showroom, open 24/7!"
Nice to have
• Photos of our fences - you can find more on our website at www.GetBrambleRail.com or Facebook.com/MeadowlarkRailGPV
Should not have
• Flashy designs

```html
<!DOCTYPE html>
<html lang="en">
<head>
<meta charset="utf-8">
<title>Frostline Picket Days Flyer</title>
<link href="https://fonts.googleapis.com/css2?family=Lobster&family=Titan+One&family=Montserrat:wght@500;700&family=Exo+2:wght@700;800&display=swap" rel="stylesheet">
<style>
  :root{
    --brand-blue:#3a82c8;
    --deep-blue:#2f6fb3;
    --bark:#4a3326;
    --ink:#1f1f1f;
    --paper:#ffffff;
    --frost:#eef1f4;
  }
  *{margin:0;padding:0;box-sizing:border-box}
  html,body{width:703px;height:1200px;overflow:hidden;background:var(--paper)}
  .flyer{position:relative;width:703px;height:1200px;overflow:hidden;
    background:radial-gradient(ellipse at 10% 10%,var(--frost),var(--paper) 55%),var(--paper);
    font-family:"Montserrat",sans-serif;color:var(--ink)}
  .brand{position:absolute;top:34px;left:0;width:100%;display:flex;justify-content:center;align-items:center;gap:12px}
  .brand-mark{width:22px;height:22px;background:var(--bark)}
  .brand-text{display:flex;flex-direction:column;line-height:1.05}
  .brand-name{font-family:"Exo 2",sans-serif;font-weight:800;font-size:25px;color:var(--brand-blue)}
  .brand-phone{font-family:"Exo 2",sans-serif;font-weight:800;font-size:23px;color:var(--ink)}
  .brand-tagline{font-family:"Exo 2",sans-serif;font-weight:700;font-size:8px;color:var(--ink);margin-top:3px}
  .headline{position:absolute;top:118px;left:0;width:100%;text-align:center}
  .headline-script{display:block;font-family:"Lobster",cursive;font-size:98px;line-height:1;color:var(--bark)}
  .headline-main{display:block;margin-top:14px;font-family:"Titan One",sans-serif;font-size:66px;letter-spacing:3px;line-height:1;color:var(--brand-blue)}
  .gallery{position:absolute;top:0;left:0}
  .offer{position:absolute;top:960px;text-align:center;font-size:21px;line-height:1.05;font-weight:500}
  .offer-price{left:40px;width:280px}
  .offer-showroom{left:386px;width:282px}
  .offer-badge{display:inline-block;margin-top:20px;width:186px;height:66px;border-radius:8px;background:var(--bark);color:var(--paper);
    font-family:"Montserrat",sans-serif;font-weight:700;font-size:46px;line-height:66px;letter-spacing:-1px}
  .offer-badge sup{font-size:22px;vertical-align:top;line-height:40px;margin-right:4px}
  .footer{position:absolute;left:0;bottom:0;width:703px;height:72px}
  .footer-info{position:absolute;left:0;bottom:6px;width:100%;text-align:center;color:var(--paper);font-size:11px;font-weight:500;line-height:1.9}
  .footer-info span{display:inline-flex;align-items:center;gap:4px;margin:0 8px}
  .footer-info svg{width:10px;height:10px;fill:var(--paper)}
</style>
</head>
<body>
<main class="flyer">
  <svg class="gallery" width="703" height="1200" viewBox="0 0 703 1200">
    <defs>
      <linearGradient id="yard" x1="0" y1="0" x2="0" y2="1">
        <stop offset="0" stop-color="#9aa6b4"/>
        <stop offset="0.3" stop-color="#7a6a5a"/>
        <stop offset="0.42" stop-color="#e2cd94"/>
        <stop offset="0.85" stop-color="#d6bd80"/>
        <stop offset="1" stop-color="#8a6a48"/>
      </linearGradient>
      <linearGradient id="fade" x1="0" y1="0" x2="0" y2="1">
        <stop offset="0" stop-color="#ffffff" stop-opacity="1"/>
        <stop offset="1" stop-color="#ffffff" stop-opacity="0"/>
      </linearGradient>
      <linearGradient id="lawn" x1="0" y1="0" x2="0" y2="1">
        <stop offset="0" stop-color="#e6e8ea"/>
        <stop offset="0.45" stop-color="#3c3c34"/>
        <stop offset="0.6" stop-color="#4f8a3a"/>
        <stop offset="1" stop-color="#8a5a3a"/>
      </linearGradient>
      <linearGradient id="woodyard" x1="0" y1="0" x2="0" y2="1">
        <stop offset="0" stop-color="#5d8a4a"/>
        <stop offset="0.4" stop-color="#86a85c"/>
        <stop offset="0.55" stop-color="#d4bb86"/>
        <stop offset="1" stop-color="#b99868"/>
      </linearGradient>
      <linearGradient id="sidegate" x1="0" y1="0" x2="1" y2="1">
        <stop offset="0" stop-color="#c9ccd0"/>
        <stop offset="0.3" stop-color="#e0c890"/>
        <stop offset="1" stop-color="#b59868"/>
      </linearGradient>
    </defs>
    <g role="img" aria-label="Photo of a long new wooden privacy fence along a brick home in winter">
      <rect x="0" y="380" width="703" height="360" fill="url(#yard)"/>
      <rect x="0" y="370" width="703" height="110" fill="url(#fade)"/>
    </g>
    <polygon points="0,718 145,860 351,995 558,860 703,718 703,1200 0,1200" fill="#ffffff"/>
    <polyline points="0,718 145,860 351,995 558,860 703,718" fill="none" stroke="var(--brand-blue)" stroke-width="3"/>
    <g role="img" aria-label="Photo of a black metal fence in front of a white two-story house">
      <polygon points="145,643 242,699 242,856 145,912 48,856 48,699" fill="url(#lawn)" stroke="var(--brand-blue)" stroke-width="3"/>
    </g>
    <g role="img" aria-label="Photo of a wooden gate and rail fence around a green backyard">
      <polygon points="558,643 655,699 655,856 558,912 461,856 461,699" fill="url(#sidegate)" stroke="var(--brand-blue)" stroke-width="3"/>
    </g>
    <g role="img" aria-label="Photo of a wooden side-yard privacy fence beside a house">
      <polygon points="351,648 498,733 498,903 351,988 204,903 204,733" fill="url(#woodyard)" stroke="var(--brand-blue)" stroke-width="3"/>
    </g>
    <path d="M0 1176 H150 C165 1176 160 1129 185 1129 H518 C543 1129 538 1176 553 1176 H703 V1200 H0 Z" fill="var(--brand-blue)"/>
  </svg>

  <header class="brand">
    <span class="brand-mark"></span>
    <div class="brand-text">
      <span class="brand-name">Bramble Rail</span>
      <span class="brand-phone">704-555-0148</span>
      <span class="brand-tagline">"Because Good Fences Make Good Neighbors"</span>
    </div>
  </header>

  <h1 class="headline">
    <span class="headline-script">Frostline</span>
    <span class="headline-main">PICKET DAYS</span>
  </h1>

  <section class="offer offer-price">
    <p>Wood fences<br>starting at</p>
    <div class="offer-badge"><sup>$</sup>12/FT!</div>
  </section>
  <section class="offer offer-showroom">
    <p>Come visit our<br>outdoor showroom, open</p>
    <div class="offer-badge">24/7</div>
  </section>

  <footer class="footer">
    <div class="footer-info">
      <span><svg viewBox="0 0 10 10"><path d="M5 0a3.5 3.5 0 0 0-3.5 3.5C1.5 6 5 10 5 10s3.5-4 3.5-6.5A3.5 3.5 0 0 0 5 0zm0 5a1.4 1.4 0 1 1 0-2.8A1.4 1.4 0 0 1 5 5z"/></svg>436 Quillen rd, Monroe, NC 28117</span><br>
      <span><svg viewBox="0 0 10 10"><path d="M0 2h10v6H0z M0 2l5 3.5L10 2" stroke="#3a82c8" stroke-width="0.8"/></svg>office@getbramblerail.com</span>
      <span><svg viewBox="0 0 10 10"><circle cx="5" cy="5" r="4.5"/></svg>getbramblerail.com</span>
    </div>
  </footer>
</main>
</body>
</html>
```